Placing my newer logo on my existing business card

I have a business card that I had you guys do years ago, then I changed my logo, I love both my business card and my logo. The challenge is both my logo and my business card are very similar in color. So I'm not sure how to make my logo stand out.

Sick

```html
<!DOCTYPE html>
<html lang="en">
<head>
<meta charset="utf-8">
<title>Summit Vitality &amp; Hormone Center – Business Card</title>
<link href="https://fonts.googleapis.com/css2?family=Cinzel:wght@500;600&family=Tinos:wght@400;700&display=swap" rel="stylesheet">
<style>
  :root {
    --rust: #b0462a;
    --rust-dark: #96361f;
    --ink: #1a1a1a;
    --sky-light: #ffffff;
    --sky-mid: #bfeaf6;
    --sky-deep: #4fd0ef;
    --backdrop: #e9ecef;
    --photo-warm: #d9c3ae;
  }
  * { box-sizing: border-box; margin: 0; padding: 0; }
  html, body { width: 1200px; height: 840px; overflow: hidden; }
  body {
    background: var(--backdrop);
    font-family: "Tinos", "Times New Roman", serif;
    color: var(--ink);
    position: relative;
  }
  .card {
    position: absolute;
    left: 270px;
    width: 660px;
    height: 377px;
    border-radius: 22px;
    overflow: hidden;
    background: linear-gradient(180deg, var(--sky-light) 0%, var(--sky-mid) 50%, var(--sky-deep) 100%);
    border-bottom: 5px solid var(--rust);
    box-shadow: 0 10px 24px rgba(0,0,0,.18);
  }
  /* ---------- back ---------- */
  .card--back { top: 26px; }
  .conditions-title {
    position: absolute;
    left: 50%; top: 30px;
    transform: translateX(-50%);
    background: var(--rust);
    color: #fff;
    font-weight: 700;
    font-size: 19px;
    padding: 6px 26px;
    border-radius: 20px;
    white-space: nowrap;
    letter-spacing: .3px;
  }
  .conditions-list {
    position: absolute;
    top: 80px;
    list-style: none;
    font-size: 17px;
    line-height: 21px;
  }
  .conditions-list li::before {
    content: "";
    display: inline-block;
    width: 6px; height: 6px;
    border-radius: 50%;
    background: var(--rust);
    margin-right: 6px;
    vertical-align: middle;
  }
  .conditions-list--left { left: 52px; }
  .conditions-list--right { left: 352px; }
  .call-line {
    position: absolute;
    left: 352px; top: 292px;
    font-size: 17px;
    line-height: 28px;
    white-space: nowrap;
  }
  .call-line .call-phone {
    color: var(--rust);
    font-size: 25px;
    font-weight: 700;
  }
  .web-line {
    position: absolute;
    left: 52px; right: 40px; top: 332px;
    display: flex; align-items: center; gap: 10px;
    font-size: 17px;
  }
  .web-line .rule { flex: 1; height: 1.5px; background: var(--ink); }
  /* ---------- front ---------- */
  .card--front { top: 433px; }
  .portrait {
    position: absolute;
    left: 95px; top: 78px;
    width: 200px; height: 299px;
    background: linear-gradient(180deg, var(--photo-warm) 0%, #f3efe9 55%, #ffffff 100%);
    border-radius: 6px 6px 0 0;
    z-index: 2;
  }
  .address-band {
    position: absolute;
    left: 0; right: 0; bottom: 0;
    height: 66px;
    background: linear-gradient(180deg, var(--rust) 0%, var(--rust-dark) 100%);
    color: #fff;
    font-size: 16px;
    display: flex; align-items: center;
    padding-left: 308px;
    padding-right: 14px;
    white-space: nowrap;
  }
  .brand {
    position: absolute;
    left: 330px; top: 28px;
    width: 300px;
    text-align: center;
  }
  .brand-mark {
    width: 46px; height: 46px;
    border-radius: 50%;
    background: var(--rust);
    margin: 0 auto 12px;
  }
  .brand-name {
    font-family: "Cinzel", "Times New Roman", serif;
    font-weight: 600;
    color: var(--rust);
    font-size: 21px;
    line-height: 25px;
    letter-spacing: 1.5px;
  }
  .contact {
    position: absolute;
    left: 330px; top: 170px;
  }
  .person-name {
    color: var(--rust);
    font-weight: 700;
    font-size: 32px;
    line-height: 34px;
  }
  .person-role { font-size: 19px; margin-bottom: 10px; }
  .contact-row {
    display: flex; align-items: center; gap: 8px;
    font-size: 17px; line-height: 24px;
  }
  .contact-row svg { width: 15px; height: 15px; flex: none; }
</style>
</head>
<body>

<section class="card card--back" aria-label="Card back">
  <div class="conditions-title">Conditions we address for women and men</div>
  <ul class="conditions-list conditions-list--left">
    <li>PCOS</li>
    <li>Hysterectomy</li>
    <li>Type-II Diabetes</li>
    <li>Insulin Resistance</li>
    <li>Hypothyroid</li>
    <li>Underactive Thyroid</li>
    <li>Fibromyalgia</li>
    <li>Chronic Fatigue</li>
    <li>Chronic Headaches &amp; Migraines</li>
    <li>Hypertension</li>
    <li>Elevated Fasting Glucose</li>
  </ul>
  <ul class="conditions-list conditions-list--right">
    <li>Pre-Diabetes</li>
    <li>Abdominal Obesity</li>
    <li>High Triglycerides</li>
    <li>High Blood Pressure</li>
    <li>High Cholesterol</li>
    <li>Gestational Diabetes</li>
    <li>Epstein Barr</li>
    <li>Infertility</li>
    <li>Infertility Drugs</li>
    <li>Anti-Depression Medications</li>
  </ul>
  <p class="call-line">Call Today!: <span class="call-phone">(555) 014-2290</span></p>
  <div class="web-line"><span class="rule"></span><span>www.summitvitalityclinic.com</span><span class="rule"></span></div>
</section>

<section class="card card--front" aria-label="Card front">
  <div class="portrait" role="img" aria-label="Portrait photo of the director in a white coat"></div>

  <div class="brand">
    <div class="brand-mark"></div>
    <div class="brand-name">Summit Vitality<br>&amp; Hormone Center</div>
  </div>

  <div class="contact">
    <div class="person-name">Marissa Halvorsen</div>
    <div class="person-role">Director</div>
    <div class="contact-row">
      <svg viewBox="0 0 24 24" aria-hidden="true"><path fill="#b0462a" d="M6.6 10.8a15.1 15.1 0 0 0 6.6 6.6l2.2-2.2c.3-.3.7-.4 1-.2 1.1.4 2.3.6 3.6.6.6 0 1 .4 1 1V20c0 .6-.4 1-1 1A17 17 0 0 1 3 4c0-.6.4-1 1-1h3.5c.6 0 1 .4 1 1 0 1.3.2 2.5.6 3.6.1.3 0 .7-.2 1z"/></svg>
      <span>1 (555) 014-2290</span>
    </div>
    <div class="contact-row">
      <svg viewBox="0 0 24 24" aria-hidden="true"><path fill="#b0462a" d="M12 2a7 7 0 0 0-7 7c0 5 7 13 7 13s7-8 7-13a7 7 0 0 0-7-7zm0 9.5A2.5 2.5 0 1 1 12 6.5a2.5 2.5 0 0 1 0 5z"/></svg>
      <span>www.summitvitalityclinic.com</span>
    </div>
  </div>

  <div class="address-band">1180 Cedar Ridge Rd Ste #5, Millbrook Utah 84000</div>
</section>

</body>
</html>
```